Refresh web site from year 2003

Voltaro Works has a web site (https://vowrk-site.no/) from early 2000 that needs to be refreshed.

Attached are company logo, favicon files, a licensed image to be used, an animation that illustrate the use of one of the products.

Target Market(s)

Industrial customers

Industry/Entity Type

Electrical Switch Board Builders, Automation Industry

Coding

Coded - Design and coding required

Number of Pages Required

3 page

Requirements
Must have
• WordPress site. Use attached animation in the front page (source file is in Adobe Animation format, if adjustments are needed). Product page for two products, "KTR" and "QX-7 Ver B".
Nice to have
• The site should focus on promoting two products KTR and QX-7 Ver B.

```html
<!DOCTYPE html>
<html lang="en">
<head>
<meta charset="utf-8">
<title>Voltaro Works</title>
<link href="https://fonts.googleapis.com/css2?family=Rubik:wght@400;500;600&family=Mulish:wght@400;500;600;700&display=swap" rel="stylesheet">
<style>
:root{
  --navy:#0b4a85;
  --blue:#2f64d0;
  --red:#d0102a;
  --ink:#1f1f24;
  --muted:#3c3c44;
  --card:#f2f5f8;
  --footer:#2a2627;
  --field:#4a4647;
  --white:#ffffff;
}
*{margin:0;padding:0;box-sizing:border-box}
html,body{width:1200px;height:2771px;overflow:hidden}
body{position:relative;font-family:"Mulish",sans-serif;color:var(--ink);background:var(--white)}
.abs{position:absolute}
.head{font-family:"Rubik",sans-serif}

/* header */
.site-header{position:absolute;left:0;top:0;width:1200px;height:119px;background:var(--white);z-index:3}
.brand{position:absolute;left:88px;top:38px;font-family:"Mulish",sans-serif;font-weight:700;font-size:34px;color:var(--navy);letter-spacing:.5px}
.call{position:absolute;left:700px;top:28px;font-size:17px;font-family:"Rubik",sans-serif;color:var(--ink)}
.call span{color:var(--blue)}
.social-top{position:absolute;top:23px;display:flex;gap:6px;left:898px}
.social-top i{display:block;width:33px;height:33px;border:1.5px solid var(--red);border-radius:50%}
.lang{position:absolute;left:1031px;top:23px;width:80px;height:32px;border-radius:16px;background:var(--blue);color:#fff;font-size:11px;font-weight:700;padding:9px 0 0 17px}
.lang svg{position:absolute;right:16px;top:12px}
.nav{position:absolute;top:77px;left:553px;display:flex;gap:0;font-size:14px;font-weight:600}
.nav a{color:var(--ink);text-decoration:none;margin-right:59px}
.nav a.active{color:var(--red)}
.nav a:last-child{margin-right:0}

/* hero */
.hero{position:absolute;left:0;top:119px;width:1200px;height:720px;background:linear-gradient(100deg,#3d4148 0%,#6b6f75 30%,#8d8f91 55%,#76787a 80%,#5d5f62 100%)}
.hero-text{position:absolute;left:0;top:244px;width:1200px;text-align:center;color:#fff;font-family:"Rubik",sans-serif}
.hero-text .eyebrow{font-size:19px;font-weight:400;margin-bottom:6px}
.hero-text h1{font-size:40px;font-weight:600;line-height:46px;text-transform:uppercase}
.btn{position:absolute;display:block;border-radius:18px;color:#fff;font-size:13px;font-weight:700;text-align:center;font-family:"Rubik",sans-serif}
.btn.red{background:var(--red)}
.btn.blue{background:var(--blue)}

/* product cards */
.card{position:absolute;top:667px;width:376px;height:454px;background:var(--card);border-bottom:3px solid var(--blue);z-index:2}
.card .shot{position:absolute;background:linear-gradient(135deg,#c9c3be,#8b8580)}
.card .band{position:absolute;left:0;top:223px;width:345px;height:40px}
.card .band span{position:absolute;left:31px;top:8px;color:#fff;font-family:"Rubik",sans-serif;font-size:19px;font-weight:500}
.card ul{position:absolute;left:34px;top:287px;list-style:none;font-size:15px;line-height:19.5px;color:var(--ink)}
.card li{position:relative;padding-left:24px}
.card li::before{content:"";position:absolute;left:0;top:4px;width:11px;height:11px;border:1.5px solid var(--red);border-radius:50%}

/* services */
.services-title{position:absolute;left:0;top:1276px;width:1200px;text-align:center;color:#fff;font-family:"Rubik",sans-serif;font-size:28px;font-weight:500;z-index:2}
.service{position:absolute;top:1340px;width:330px;text-align:center;color:#fff;z-index:2}
.service svg{display:block;margin:0 auto}
.service h3{font-family:"Rubik",sans-serif;font-size:20px;font-weight:500;margin-top:22px}
.service p{font-size:13px;font-weight:600;line-height:19px;margin-top:18px}

/* about */
.about-photo{position:absolute;left:88px;top:1824px;width:448px;height:448px;border-radius:50%;background:linear-gradient(120deg,#5a5e64,#c7c9cb 45%,#e5e3de 70%,#9a9c9f)}
.about{position:absolute;left:616px;top:1846px;width:500px}
.about h2{font-family:"Rubik",sans-serif;font-size:28px;font-weight:500;color:var(--ink)}
.about h2 span{color:var(--navy)}
.about h4{font-family:"Rubik",sans-serif;font-size:14px;font-weight:500;line-height:19px;margin-top:14px;text-transform:uppercase}
.about p{font-size:13px;line-height:19px;color:var(--muted);margin-top:19px}

/* footer */
.footer{position:absolute;left:0;top:2352px;width:1200px;height:419px;background:var(--footer);color:#fff}
.footer .brand-f{position:absolute;left:88px;top:62px;font-weight:700;font-size:40px;color:#fff}
.footer .ceo{position:absolute;left:149px;top:216px;font-size:14px}
.footer .lbl{color:var(--blue)}
.footer h5{position:absolute;font-family:"Rubik",sans-serif;font-size:14px;font-weight:500}
.footer .txt{position:absolute;font-size:14px;line-height:19px}
.footer .fcall{position:absolute;left:440px;top:98px;font-size:20px;color:var(--blue)}
.fsoc{position:absolute;left:440px;top:2640px}
.fsoc i{position:absolute;top:0;width:32px;height:32px;border-radius:50%}
.field{position:absolute;background:var(--field);color:#d8d8d8;font-size:12px;padding:8px 0 0 15px}
.legal{position:absolute;left:88px;top:380px;font-size:14px}
.legal span{color:var(--blue)}
.fnav{position:absolute;top:383px;left:439px;display:flex;font-size:14px}
.fnav a{color:#fff;text-decoration:none;margin-right:44px}
</style>
</head>
<body>

<header class="site-header">
  <div class="brand">Voltaro Works</div>
  <div class="call"><span>Call Us:</span>
    <svg width="14" height="14" viewBox="0 0 24 24" fill="none" stroke="#2f64d0" stroke-width="2" style="vertical-align:-1px"><path d="M22 16.9v3a2 2 0 0 1-2.2 2 19.8 19.8 0 0 1-8.6-3.1 19.5 19.5 0 0 1-6-6A19.8 19.8 0 0 1 2.1 4.2 2 2 0 0 1 4.1 2h3a2 2 0 0 1 2 1.7c.1 1 .4 1.9.7 2.8a2 2 0 0 1-.5 2.1L8 9.9a16 16 0 0 0 6 6l1.3-1.3a2 2 0 0 1 2.1-.4c.9.3 1.8.6 2.8.7a2 2 0 0 1 1.7 2z"/></svg>
    +47 900 00 123</div>
  <div class="social-top"><i></i><i></i><i></i></div>
  <div class="lang">ENG
    <svg width="10" height="7" viewBox="0 0 10 7"><path d="M1 1l4 4 4-4" stroke="#fff" stroke-width="1.5" fill="none"/></svg></div>
  <nav class="nav">
    <a class="active" href="#">-- Home --</a>
    <a href="#">About Us</a>
    <a href="#">Services</a>
    <a href="#">Products</a>
    <a href="#">Contact Us</a>
  </nav>
</header>

<section class="hero" role="img" aria-label="Photo of industrial electrical switchboard cabinets with meters and control switches"></section>
<div class="hero-text">
  <div class="eyebrow">OUR MISSION IS TO</div>
  <h1>Contribute good and cost effective<br>electronics products for the<br>industrial market</h1>
</div>
<a class="btn red" style="left:535px;top:442px;width:128px;height:31px;padding-top:8px">Contact Us</a>
<svg class="abs" style="left:72px;top:368px" width="16" height="30" viewBox="0 0 16 30"><path d="M14 2L2 15l12 13" stroke="#fff" stroke-width="2" fill="none"/></svg>
<svg class="abs" style="left:1111px;top:368px" width="16" height="30" viewBox="0 0 16 30"><path d="M2 2l12 13L2 28" stroke="#fff" stroke-width="2" fill="none"/></svg>
<svg class="abs" style="left:590px;top:601px" width="20" height="16" viewBox="0 0 20 16"><path d="M2 2l8 7 8-7M2 8l8 7 8-7" stroke="#fff" stroke-width="1.5" fill="none"/></svg>

<svg class="abs" style="left:0;top:720px" width="1200" height="125" viewBox="0 0 1200 125">
  <path d="M0 70 C150 120 300 125 450 105 C650 80 800 10 1000 20 C1100 25 1160 60 1200 70 L1200 125 L0 125 Z" fill="#fff"/>
  <path d="M0 70 C150 120 300 125 450 105 C650 80 800 10 1000 20 C1100 25 1160 60 1200 70" stroke="#2f64d0" stroke-width="10" fill="none"/>
</svg>

<article class="card" style="left:208px">
  <div class="shot" style="left:80px;top:40px;width:222px;height:140px;border-radius:40px 40px 12px 12px" role="img" aria-label="Product photo of the KTR indicator lamp"></div>
  <svg class="band" viewBox="0 0 345 40"><path d="M0 0H313L345 40H0Z" fill="#0b4a85"/></svg>
  <div class="band"><span>KTR</span></div>
  <ul>
    <li>Very long operating time.</li>
    <li>Easy mounting</li>
    <li>Reliable reading at long distance</li>
    <li>Wide angle</li>
  </ul>
  <a class="btn blue" style="left:33px;top:392px;width:96px;height:31px;padding-top:8px">Read More</a>
</article>

<article class="card" style="left:616px">
  <div class="shot" style="left:89px;top:36px;width:181px;height:160px;background:linear-gradient(90deg,#d8dde2 0 48%,#3f6a55 52% 100%)" role="img" aria-label="Product photo of the QX-7 Ver B module housing and circuit board"></div>
  <svg class="band" viewBox="0 0 345 40"><path d="M0 0H313L345 40H0Z" fill="#0b4a85"/></svg>
  <div class="band"><span>QX-7 Ver B</span></div>
  <ul>
    <li>Interlocking of switch controls the power<br>and transformer stations.</li>
    <li style="margin-top:19px">Voltage indication of lines / bus bars.</li>
  </ul>
  <a class="btn red" style="left:33px;top:392px;width:96px;height:31px;padding-top:8px">Read More</a>
</article>

<!-- services band -->
<svg class="abs" style="left:0;top:1202px" width="1200" height="570" viewBox="0 0 1200 570">
  <defs><linearGradient id="svc" x1="0" y1="0" x2="1" y2="1"><stop offset="0" stop-color="#0b4a85"/><stop offset="1" stop-color="#0d4f92"/></linearGradient></defs>
  <path d="M0 0H1200V450 C1100 430 1000 420 880 430 C700 445 450 560 260 565 C150 568 60 530 0 490 Z" fill="url(#svc)"/>
  <path d="M1200 450 C1100 430 1000 420 880 430 C700 445 450 560 260 565 C150 568 60 530 0 490" stroke="#2f64d0" stroke-width="10" fill="none"/>
</svg>
<h2 class="services-title">OUR SERVICES</h2>

<div class="service" style="left:83px">
  <svg width="80" height="80" viewBox="0 0 80 80" fill="none" stroke="#fff" stroke-width="2.5"><circle cx="40" cy="40" r="12"/><circle cx="40" cy="40" r="22" stroke-dasharray="9 5"/><path d="M14 30a28 28 0 0 1 44-14M66 50a28 28 0 0 1-44 14"/><path d="M54 10l4 6-7 1M26 70l-4-6 7-1"/></svg>
  <h3>PRODUCTION</h3>
  <p>Small series production of electronic units in the<br>number of 10 to 200 units.</p>
</div>
<div class="service" style="left:435px">
  <svg width="80" height="80" viewBox="0 0 80 80" fill="none" stroke="#fff" stroke-width="2.5"><path d="M6 42l18-16 12 10 30-26"/><path d="M52 8h16v16"/><circle cx="40" cy="64" r="10"/><path d="M20 78a20 20 0 0 1 40 0M40 48v-6M28 54l-4-4M52 54l4-4"/></svg>
  <h3>DEVOLEPMENT</h3>
  <p>Development of product concept to finished product<br>in collaboration with a customer.</p>
</div>
<div class="service" style="left:787px">
  <svg width="80" height="80" viewBox="0 0 80 80" fill="none" stroke="#fff" stroke-width="2.5"><path d="M8 10h46v10M8 10v64h64V40"/><path d="M8 20h-4M8 30h-4M8 40h-4M8 50h-4M8 60h-4"/><path d="M26 56l4-14 36-36 10 10-36 36z"/><path d="M46 74l26-26v26z"/></svg>
  <h3>DESIGN</h3>
  <p>Designing of electronics and print cards for<br>pre-assembled and tested unit.</p>
</div>
<a class="btn blue" style="left:536px;top:1559px;width:128px;height:31px;padding-top:8px;z-index:2">Explore More</a>

<!-- about -->
<div class="about-photo" role="img" aria-label="Close photo of switchboard cabinet doors with meters and rotary switches"></div>
<section class="about">
  <h2>ABOUT THE <span>VOLTARO WORKS</span></h2>
  <h4>Voltaro Works is a production and development company for electronics with emphasis on small series production.</h4>
  <p>We are today two employees with good and relevant access to additional expertise in the established network. The company was established in 1985 and has since 2001 taken over production equipment and production basis from another company in the same industry.</p>
  <p>Norvik Electronics' production department for electronics was decommissioned and sold July 2001. Voltaro Works v/Sindre Holmvik has taken over production drawings and equipment.</p>
  <p>Our mission is to contribute good and cost effective electronics products for the industrial market, as well as seek and develop solutions to new and existing concepts.</p>
</section>
<a class="btn red" style="left:616px;top:2214px;width:128px;height:31px;padding-top:8px">Discover More</a>

<footer class="footer">
  <div class="brand-f">Voltaro Works</div>
  <div class="ceo"><span class="lbl">CEO:</span> Sindre Holmvik</div>

  <h5 style="left:440px;top:66px">CONTACT US</h5>
  <div class="fcall">Call: +47 900 00 123</div>
  <div class="txt" style="left:440px;top:124px"><span class="lbl">e.</span> post@vowrk-site.no</div>
  <div class="txt" style="left:440px;top:160px"><span class="lbl" style="font-size:13px">Address:</span><br>Bekkeveien 42 N-4000<br>Dalstrand Norway</div>
  <h5 style="left:440px;top:250px">FOLLOW US</h5>
  <div style="position:absolute;left:440px;top:288px">
    <i style="position:absolute;left:0;width:32px;height:32px;border-radius:50%;background:#2f64d0"></i>
    <i style="position:absolute;left:40px;width:32px;height:32px;border-radius:50%;background:#d0102a"></i>
    <i style="position:absolute;left:80px;width:32px;height:32px;border-radius:50%;background:#2f64d0"></i>
  </div>

  <h5 style="left:751px;top:66px">SEND US MESSAGE</h5>
  <div class="field" style="left:751px;top:104px;width:172px;height:32px">Name</div>
  <div class="field" style="left:940px;top:104px;width:172px;height:32px">Phone</div>
  <div class="field" style="left:751px;top:153px;width:361px;height:31px">Email</div>
  <div class="field" style="left:751px;top:201px;width:361px;height:71px">Message</div>
  <a class="btn red" style="left:751px;top:289px;width:111px;height:31px;padding-top:8px">Submit</a>

  <div class="legal">© 2022 <span>Voltaro Works</span>. All Right Reserved</div>
  <nav class="fnav"><a href="#">Home</a><a href="#">About Us</a><a href="#">Services</a><a href="#">Products</a><a href="#">Contact Us</a></nav>
  <svg class="abs" style="left:1144px;top:348px" width="24" height="28" viewBox="0 0 24 28"><path d="M12 2L2 26l10-7 10 7z" stroke="#2f64d0" stroke-width="2" fill="none"/></svg>
</footer>

</body>
</html>
```